Gourmet food company looking for a dazzling label for their premuim vinagrette dressings

Need a food label that will dazzle our customer and prove what a premium product we have. We make high end gourmet dressing for vegetables, fruit, meat, poultry and fish.

Our label will fit on a 250 mil Tolvenka Square bottle. Labels should be a 4x5 or even 5x5 depending on the design. Nutritionals, bar codes and company blurb will be supplied later. We really want to test you all's talent on this one and are very excited to see your renderings!

Our dressings are Champagne Pear Vinaigrette, White Balsmic Vinaigrette, Mojito Lime Vinaigrette, Creamy-Avacado Lime Vinaigrette, and Asian Sesame Vinaigrette. I hope these names will help you envision our product and kinda what we are looking for.
Updates

Thank you all so far for your renderings.I really don't want pictures if that helps. Our logo can be smaller and/or the name of the product bigger. Perhaps we can even redesign Velora and remove the leaf as I don't really care for what I see yet.So good luck and thanks Added Friday, August 19, 2016

I am still looking for that clean - elegant design for our product as our product is just that. If you look on the internet at vinegars and oils you will see many designs that are simple yet elegant. Creative lettering, bordering, color (can be black and white) and size will help accomplish this. So I invite you to use all your creativity and help me find just what we need.Many thanks Added Tuesday, August 23, 2016

Project Deadline Extended Reason: So many great designs coming in that I wanted a few extra days to tweek!Great job all Added Friday, August 26, 2016

Project Deadline Extended Reason: Very good designs thus far. We just need a few more days.Thanks Added Wednesday, August 31, 2016

Target Market(s)

High end grocery and specialty stores.

Our side panel on the label will say "At Velora we're fanatics for great flavors and are passionate about finding the best ingredients. From simple to elegant our products are "simply velora".

Industry/Entity Type

It Company

Font styles to use
Serif
Decorative
Script

Requirements
Must have
• A label that will draw the consumer to pick it up! Need something bold and elegant...
Nice to have
• Again, I really would like to have a label that pops. Since the bottle front is only about 2inches in width it will need some creativity. Would like something very simple and elegant.
• If the designer does not like the logo, please feel free to design without it!
Should not have
• Dark dark colors. We are selling dressing and we don't want any colors that may distort the contents.
• No stock photos for the front. I don't want our dressing to look like the others on the self. Brambleth Kitchen just uses lettering and a their packaging is eye catching

```html
<!DOCTYPE html>
<html lang="en">
<head>
<meta charset="utf-8">
<title>Velora Vinaigrette Labels</title>
<link rel="stylesheet" href="https://fonts.googleapis.com/css2?family=Rokkitt:wght@200;400;500&display=swap">
<style>
  :root {
    --canvas-bg: #eef0e8;
    --frame-line: rgba(255, 255, 255, 0.85);
    --name-ink: #fdf7f6;
    --sesame-light: #f6d3da;
    --sesame-mid: #eeaabb;
    --sesame-deep: #e07c96;
    --sesame-ink: #d63f6a;
    --avocado-light: #cfe3cf;
    --avocado-mid: #8fbf97;
    --avocado-deep: #4f8f63;
    --avocado-ink: #3d7448;
    --type-ink: #ffffff;
  }

  * { box-sizing: border-box; margin: 0; padding: 0; }

  html, body {
    width: 1200px;
    height: 1000px;
    overflow: hidden;
    background: var(--canvas-bg);
  }

  .label-sheet {
    width: 1200px;
    height: 1000px;
    display: flex;
    justify-content: center;
    align-items: center;
    gap: 180px;
  }

  .label {
    position: relative;
    width: 260px;
    height: 670px;
    box-shadow: 0 6px 18px rgba(60, 70, 50, 0.18);
  }

  .label__wash {
    position: absolute;
    inset: 0;
  }

  .label--sesame .label__wash {
    background:
      radial-gradient(ellipse at 70% 80%, var(--sesame-deep) 0%, transparent 60%),
      radial-gradient(ellipse at 20% 20%, var(--sesame-light) 0%, transparent 70%),
      linear-gradient(160deg, var(--sesame-light) 0%, var(--sesame-mid) 55%, var(--sesame-deep) 100%);
  }

  .label--avocado .label__wash {
    background:
      radial-gradient(ellipse at 30% 25%, var(--avocado-deep) 0%, transparent 60%),
      radial-gradient(ellipse at 75% 85%, var(--avocado-light) 0%, transparent 65%),
      linear-gradient(200deg, var(--avocado-mid) 0%, var(--avocado-deep) 50%, var(--avocado-light) 100%);
  }

  .label__frame {
    position: absolute;
    inset: 10px;
    border: 2px solid var(--frame-line);
  }

  .label__type {
    position: absolute;
    top: 28px;
    bottom: 28px;
    left: 22px;
    right: 22px;
    writing-mode: vertical-rl;
    transform: rotate(180deg);
    display: flex;
    flex-direction: column;
    font-family: "Rokkitt", Georgia, serif;
  }

  .label__brand {
    font-weight: 200;
    font-size: 168px;
    line-height: 0.9;
    color: var(--name-ink);
    letter-spacing: 2px;
    text-align: start;
  }

  .label__flavour {
    font-weight: 500;
    font-size: 31px;
    line-height: 1.05;
    letter-spacing: 1px;
    text-transform: uppercase;
    text-align: end;
    margin-top: 6px;
  }

  .label--sesame .label__flavour { color: var(--sesame-ink); }
  .label--avocado .label__flavour { color: var(--avocado-ink); }

  .label__kind {
    font-weight: 400;
    font-size: 26px;
    line-height: 1.05;
    letter-spacing: 2px;
    text-transform: uppercase;
    text-align: end;
    color: var(--type-ink);
  }

  .label__volume {
    position: absolute;
    right: 34px;
    bottom: 34px;
    font-family: "Rokkitt", Georgia, serif;
    font-weight: 500;
    font-size: 14px;
    letter-spacing: 0.5px;
    color: var(--type-ink);
  }
</style>
</head>
<body>
  <main class="label-sheet">
    <article class="label label--sesame">
      <div class="label__wash" role="img" aria-label="Soft pink watercolour wash texture"></div>
      <div class="label__frame"></div>
      <div class="label__type">
        <h1 class="label__brand">Velora</h1>
        <p class="label__flavour">Asian Sesame</p>
        <p class="label__kind">Vinaigrette</p>
      </div>
      <p class="label__volume">250 ML</p>
    </article>

    <article class="label label--avocado">
      <div class="label__wash" role="img" aria-label="Soft green watercolour wash texture"></div>
      <div class="label__frame"></div>
      <div class="label__type">
        <h1 class="label__brand">Velora</h1>
        <p class="label__flavour">Creamy-Avocado Lime</p>
        <p class="label__kind">Vinaigrette</p>
      </div>
      <p class="label__volume">250 ML</p>
    </article>
  </main>
</body>
</html>
```